Real Estate Sales Brokerage

Design a modern and fresh looking standard size business card, incorporate our logo's color scheme and modern appearance with head shot photo on front side and incorporate our log on the back side

Target Market(s)

Residential Home sales

Industry/Entity Type

Real Estate Agent

Font styles to use
Sans Serif

Colors

Designer to choose colors to be used in the design.

Requirements
Must have
• fresh, modern, not too busy, incorporate head shot in front of the card, incorporate logo in front and back of the card. Use logo design scheme as appropriate.
Nice to have
• horizontal and vertical options to compare would be nice.

```html
<!DOCTYPE html>
<html lang="en">
<head>
<meta charset="utf-8">
<title>Harborline Home Realty — Business Card</title>
<link href="https://fonts.googleapis.com/css2?family=Roboto+Condensed:wght@400;700&family=Roboto:wght@400;500&display=swap" rel="stylesheet">
<style>
  :root {
    --olive: #6c6d37;
    --olive-light: #7d7e42;
    --olive-dark: #5c5d2e;
    --yellow: #f2cf3a;
    --white: #ffffff;
    --stage: #2f2f2f;
    --photo-top: #f4f5f8;
    --photo-suit: #3d5c9c;
  }
  * { margin: 0; padding: 0; box-sizing: border-box; }
  html, body { width: 1200px; height: 801px; overflow: hidden; }
  body {
    background: var(--stage);
    display: flex;
    align-items: center;
    justify-content: center;
    gap: 48px;
    font-family: "Roboto", sans-serif;
  }
  .card {
    position: relative;
    width: 540px;
    height: 309px;
    overflow: hidden;
    border-radius: 2px;
    box-shadow: 0 10px 28px rgba(0,0,0,.45);
  }
  .card-shape { position: absolute; inset: 0; }

  /* Front */
  .front-info {
    position: absolute;
    left: 34px;
    top: 40px;
    color: var(--white);
  }
  .agent-name {
    font-family: "Roboto Condensed", sans-serif;
    font-weight: 700;
    font-size: 27px;
    letter-spacing: 1px;
    text-transform: uppercase;
    color: var(--yellow);
  }
  .agent-title {
    font-family: "Roboto Condensed", sans-serif;
    font-size: 13px;
    letter-spacing: 1.5px;
    text-transform: uppercase;
    margin-top: 2px;
  }
  .contact-list { list-style: none; margin-top: 22px; }
  .contact-list li {
    display: flex;
    align-items: center;
    gap: 10px;
    font-size: 13px;
    letter-spacing: .6px;
    line-height: 21px;
  }
  .contact-icon { width: 13px; height: 13px; flex: none; }
  .address { font-size: 12.5px; letter-spacing: .6px; line-height: 19px; margin-top: 10px; }
  .front-web {
    font-family: "Roboto Condensed", sans-serif;
    font-weight: 700;
    font-size: 13px;
    letter-spacing: 1px;
    margin-top: 12px;
  }

  /* Back */
  .card-back { background: linear-gradient(135deg, var(--olive-dark), var(--olive-light) 55%, var(--olive)); }
  .brand {
    position: absolute;
    left: 0; right: 0; top: 92px;
    display: flex;
    align-items: center;
    justify-content: center;
    gap: 16px;
  }
  .brand-square {
    width: 54px; height: 54px;
    border: 3px solid var(--white);
  }
  .brand-name {
    font-family: "Roboto Condensed", sans-serif;
    font-weight: 400;
    font-size: 27px;
    line-height: 29px;
    letter-spacing: 2px;
    text-transform: uppercase;
    color: var(--white);
  }
  .back-web {
    position: absolute;
    left: 0; right: 0; bottom: 62px;
    text-align: center;
    font-family: "Roboto Condensed", sans-serif;
    font-weight: 700;
    font-size: 14px;
    letter-spacing: 1.5px;
    color: var(--white);
  }
</style>
</head>
<body>

  <section class="card card-front" aria-label="Business card front">
    <svg class="card-shape" viewBox="0 0 540 309" width="540" height="309">
      <defs>
        <linearGradient id="oliveFront" x1="0" y1="0" x2="1" y2="1">
          <stop offset="0" stop-color="#5c5d2e"/>
          <stop offset="0.6" stop-color="#7d7e42"/>
          <stop offset="1" stop-color="#6c6d37"/>
        </linearGradient>
        <linearGradient id="photoTone" x1="0" y1="0" x2="0" y2="1">
          <stop offset="0" stop-color="#f4f5f8"/>
          <stop offset="0.45" stop-color="#e9e6e2"/>
          <stop offset="1" stop-color="#3d5c9c"/>
        </linearGradient>
      </defs>
      <rect class="headshot" x="290" y="0" width="250" height="309" fill="url(#photoTone)" role="img" aria-label="Headshot photo of the agent in a blue suit and red tie"/>
      <path class="olive-panel" d="M0 0 H300 C322 110 348 220 376 309 H0 Z" fill="url(#oliveFront)"/>
      <path class="accent-band" d="M300 0 C322 110 348 220 376 309 H394 C364 220 334 110 308 0 Z" fill="#f2cf3a"/>
    </svg>

    <div class="front-info">
      <h1 class="agent-name">Dale Morrow</h1>
      <p class="agent-title">Director</p>
      <ul class="contact-list">
        <li>
          <svg class="contact-icon" viewBox="0 0 13 13"><rect x="2.5" y="1" width="8" height="11" rx="1.5" fill="none" stroke="#f2cf3a" stroke-width="1.5"/></svg>
          555 014 2290
        </li>
        <li>
          <svg class="contact-icon" viewBox="0 0 13 13"><path d="M3 1 L5 1 L6 4 L4.5 5.2 C5.3 7 6.2 8 8 8.6 L9.2 7 L12 8 L12 10.5 C12 11.5 11 12 10 11.8 C5.5 11 2 7.5 1.3 3 C1.2 2 1.8 1 3 1 Z" fill="#f2cf3a"/></svg>
          555 014 2290
        </li>
        <li>
          <svg class="contact-icon" viewBox="0 0 13 13"><rect x="1" y="4" width="11" height="8" fill="#f2cf3a"/><rect x="3" y="1" width="7" height="3" fill="#f2cf3a"/></svg>
          +1 555 014 7781
        </li>
        <li>
          <svg class="contact-icon" viewBox="0 0 13 13"><rect x="1" y="2.5" width="11" height="8" fill="none" stroke="#f2cf3a" stroke-width="1.4"/><path d="M1 2.5 L6.5 7 L12 2.5" fill="none" stroke="#f2cf3a" stroke-width="1.4"/></svg>
          dale@harborlinere.com
        </li>
      </ul>
      <p class="address">418 Alder Row, Brookfield<br>CA 90871, United States</p>
      <p class="front-web">www.harborlinere.com</p>
    </div>
  </section>

  <section class="card card-back" aria-label="Business card back">
    <div class="brand">
      <span class="brand-square" aria-hidden="true"></span>
      <p class="brand-name">Harborline<br>Home<br>Realty</p>
    </div>
    <p class="back-web">www.harborlinere.com</p>
  </section>

</body>
</html>
```